Eye catching Bottle label for pink gin targeting women 25+

We need a new label for a re-launch of our shimmering strawberry pink gin liqueur. We would like it to look premium and eye catching on the shelf. We have 2 labels we require, one for 200ml bottle (2x2 inches) and one for 500ml bottle 4x4 inches). Label must state the ml of the bottle abd that it is 18.75%Vol. Also say Shimmering Strawberry Gin Liqueur with the brand name at the top - Harlow Vale Distillers. We have a logo but it doesn't need to be used if it doesn't work with the design/colours. The gin is presented in a clear bottle and is pink and sparkly. See uploaded image for reference.

Target Market(s)

Women aged 25-45

Font styles to use
Decorative

Colors
f59296
fbd4d5
eea4c8

Requirements
Must have
• Bottle size - 500ml/200ml
• Must say 18.75% Vol
• Must have brand name - Harlow Vale Distillers
• Must have product name - Glistening Blush Raspberry
• Must say - Gin Liqueur
Nice to have
• Some sort of floral or swirley background detail would be nice
Should not have
• Must not appeal to children

```html
<!DOCTYPE html>
<html lang="en">
<head>
<meta charset="utf-8">
<title>Glistening Blush Raspberry Gin Liqueur – Label</title>
<link rel="stylesheet" href="https://fonts.googleapis.com/css2?family=Emilys+Candy&family=Tinos&display=swap">
<style>
  :root {
    --band-pink: #fcc8e2;
    --stripe-pink: #f59ad9;
    --label-white: #ffffff;
    --title-pink: #f38fc0;
    --title-edge: #ee7fb4;
    --brand-ink: #3a2a30;
    --detail-pink: #f08db8;
  }
  * { margin: 0; padding: 0; box-sizing: border-box; }
  html, body {
    width: 1200px;
    height: 1200px;
    overflow: hidden;
    background: var(--label-white);
  }
  .label {
    position: relative;
    width: 1200px;
    height: 1200px;
    background: var(--label-white);
  }
  .brand-band {
    position: absolute;
    left: 0; top: 0;
    width: 1200px; height: 300px;
    background: var(--band-pink);
    display: flex;
    align-items: center;
    justify-content: center;
  }
  .brand-name {
    font-family: "Emilys Candy", cursive;
    font-weight: 400;
    font-size: 64px;
    line-height: 1.05;
    color: var(--brand-ink);
    text-align: center;
  }
  .accent-stripe {
    position: absolute;
    left: 0; top: 300px;
    width: 1200px; height: 60px;
    background: var(--stripe-pink);
  }
  .product-panel {
    position: absolute;
    left: 0; top: 360px;
    width: 1200px; height: 620px;
    background: var(--label-white);
    text-align: center;
    font-family: "Emilys Candy", cursive;
    color: var(--title-pink);
    -webkit-text-stroke: 1.5px var(--title-edge);
  }
  .product-name {
    font-weight: 400;
    text-transform: uppercase;
    letter-spacing: 2px;
  }
  .product-name .line-main {
    display: block;
    margin-top: 80px;
    font-size: 118px;
    line-height: 1;
  }
  .product-name .line-flavour {
    display: block;
    margin-top: 14px;
    font-size: 86px;
    line-height: 1;
  }
  .product-type {
    margin-top: 96px;
    font-size: 80px;
    line-height: 1;
    text-transform: uppercase;
    letter-spacing: 3px;
  }
  .info-band {
    position: absolute;
    left: 0; top: 980px;
    width: 1200px; height: 220px;
    background: var(--band-pink);
    font-family: "Tinos", serif;
    color: var(--detail-pink);
    font-size: 46px;
  }
  .volume {
    position: absolute;
    left: 62px; top: 100px;
  }
  .strength {
    position: absolute;
    right: 62px; top: 100px;
  }
</style>
</head>
<body>
  <main class="label">
    <header class="brand-band">
      <p class="brand-name">Harlow Vale<br>Distillers</p>
    </header>
    <div class="accent-stripe"></div>
    <section class="product-panel">
      <h1 class="product-name">
        <span class="line-main">Glistening</span>
        <span class="line-flavour">Blush Raspberry</span>
      </h1>
      <p class="product-type">Gin Liqueur</p>
    </section>
    <footer class="info-band">
      <span class="volume">500ml</span>
      <span class="strength">18.75% Vol</span>
    </footer>
  </main>
</body>
</html>
```